website for 'thebrightnook' which is a specialise tutoring company for children with learning difficu

We need a website for a new business that is focused on assessment and then specialised tutoring for young children with learning difficulties. The website needs to be simple but fun and fresh. We have an existing logo (uploaded) that needs to be the building block for the website. The website doesn't need to be overly content-heavy.

Target Market(s)

parents

Industry/Entity Type

Education

Number of Pages Required

3 page

Font styles to use
Other font styles liked:
• possibly matched to the logo

Requirements
Must have
• a initial front page which introduces the business and provides contact details, a second page that will allow for a more content-heavy section, a third page which focuses on introducing the staff (initially 3 staff ),

```html
<!DOCTYPE html>
<html lang="en">
<head>
<meta charset="utf-8">
<title>thebrightnook — Home</title>
<link href="https://fonts.googleapis.com/css2?family=Libre+Bodoni:wght@400;700&display=swap" rel="stylesheet">
<style>
  :root{
    --green:#7dc242;
    --green-dark:#5fa52a;
    --ink:#2b2b2b;
    --text:#555555;
    --white:#ffffff;
    --stage:#ececec;
    --band:#efefef;
    --footer:#3d3d3d;
    --footer-line:#5a5a5a;
    --button-dark:#333333;
  }
  *{box-sizing:border-box;margin:0;padding:0}
  html,body{width:1200px;height:1000px;overflow:hidden}
  body{background:var(--stage);font-family:"Libre Bodoni",Georgia,serif;color:var(--text);position:relative}
  .page{position:absolute;left:381px;top:72px;width:435px;height:870px;background:var(--white);overflow:hidden}
  .abs{position:absolute}

  .top-bar{left:0;top:0;width:100%;height:6px;background:var(--green)}

  .brand{left:40px;top:30px;display:flex;align-items:center;gap:6px}
  .brand-dot{width:12px;height:12px;border-radius:50%;background:var(--green)}
  .brand-name{font-size:15px;color:var(--ink);font-weight:400;letter-spacing:-.2px}

  .social{right:36px;top:17px;display:flex;gap:5px}
  .social span{width:11px;height:11px;border-radius:50%;background:var(--green);display:block}

  .nav{right:36px;top:38px;display:flex;gap:14px;font-size:9px;letter-spacing:.3px;color:var(--ink)}
  .nav a{color:inherit;text-decoration:none;padding-bottom:3px}
  .nav a.active{color:var(--green);border-bottom:1.5px solid var(--green)}

  .hero{left:0;top:60px;width:100%;height:191px}
  .hero-photo{position:absolute;inset:0;background:linear-gradient(160deg,#9a9a9a 0%,#6e6e6e 45%,#4a4a4a 100%)}
  .hero-title{position:absolute;left:0;right:0;top:58px;text-align:center;color:var(--white);font-size:20px;line-height:28px}
  .hero-arrow{position:absolute;top:78px}
  .hero-arrow.left{left:20px}
  .hero-arrow.right{right:20px}
  .btn{display:inline-block;background:var(--green);color:var(--white);font-size:7px;letter-spacing:.4px;padding:3px 6px;text-transform:uppercase}
  .hero .btn{position:absolute;left:190px;top:145px}

  .why-kicker{left:0;right:0;top:268px;text-align:center;font-size:7px;color:var(--green);letter-spacing:.5px}
  .why-title{left:0;right:0;top:278px;text-align:center;font-size:14px;color:var(--ink)}
  .why-rule{left:188px;top:299px;width:58px;height:2px;background:#666}

  .feature{top:319px;width:120px;text-align:center}
  .feature-icon{width:52px;height:52px;margin:0 auto;display:block}
  .feature-title{margin-top:9px;font-size:11px;letter-spacing:1.5px;color:var(--ink)}
  .feature-text{margin-top:3px;font-size:6.3px;line-height:8.3px;height:74px;overflow:hidden}
  .btn-outline{display:inline-block;margin-top:8px;border:1px solid var(--green);color:var(--text);font-size:5.5px;letter-spacing:.4px;padding:2px 8px;text-transform:uppercase}

  .band{left:0;top:500px;width:100%;height:196px;background:var(--band)}
  .band-photo{position:absolute;left:12px;top:8px;width:203px;height:135px;background:linear-gradient(135deg,#d8b58a 0%,#c97b4a 40%,#9fb4c9 100%)}
  .band-thumb{position:absolute;top:148px;width:57px;height:39px;background:linear-gradient(135deg,#d3ad84,#b66c48 50%,#8da6c0)}
  .band-title{position:absolute;left:225px;top:16px;font-size:11px;letter-spacing:1px;color:var(--ink)}
  .band-text{position:absolute;left:225px;top:36px;width:198px;font-size:7px;line-height:9.2px;text-align:justify;height:120px;overflow:hidden}
  .band .btn{position:absolute;left:225px;top:175px;font-size:5.5px;padding:2px 5px}

  .cta{left:0;top:710px;width:100%;height:44px;background:var(--green);color:var(--white)}
  .cta-title{position:absolute;left:11px;top:8px;font-size:10px;font-weight:700;letter-spacing:.3px}
  .cta-text{position:absolute;left:11px;top:22px;font-size:7.5px}
  .cta-btn{position:absolute;right:15px;top:10px;background:var(--button-dark);color:var(--white);font-size:7.5px;letter-spacing:.4px;padding:3px 6px}

  .footer{left:0;top:754px;width:100%;height:116px;background:var(--footer);color:var(--white)}
  .footer-col{position:absolute;top:12px}
  .footer-heading{font-size:10px;color:var(--green);padding-bottom:5px;border-bottom:1px solid var(--footer-line);width:70px}
  .footer-list{list-style:none;margin-top:8px;font-size:7px;line-height:17px}
  .footer-contact{margin-top:9px;font-size:6.5px;line-height:10.5px}
  .footer-contact .label{color:var(--green)}
  .footer-social{display:flex;gap:5px;margin-top:10px}
  .footer-social span{width:10px;height:10px;border-radius:50%;background:var(--green)}
  .footer-brand{position:absolute;right:11px;top:58px;display:flex;align-items:center;gap:5px}
  .footer-brand .brand-dot{width:10px;height:10px}
  .footer-brand .brand-name{color:var(--white);font-size:13px}
</style>
</head>
<body>
<main class="page">
  <div class="abs top-bar"></div>

  <header>
    <div class="abs brand"><span class="brand-dot"></span><span class="brand-name">thebrightnook</span></div>
    <div class="abs social" aria-label="Social links"><span></span><span></span><span></span><span></span></div>
    <nav class="abs nav">
      <a class="active" href="#">HOME</a><a href="#">TRAINING</a><a href="#">STAFF</a><a href="#">CONTACT US</a>
    </nav>
  </header>

  <section class="abs hero">
    <div class="hero-photo" role="img" aria-label="Black and white photo of students sitting in a row working at desks"></div>
    <svg class="hero-arrow left" width="14" height="30" viewBox="0 0 14 30"><polyline points="12,2 2,15 12,28" fill="none" stroke="#fff" stroke-width="2"/></svg>
    <svg class="hero-arrow right" width="14" height="30" viewBox="0 0 14 30"><polyline points="2,2 12,15 2,28" fill="none" stroke="#fff" stroke-width="2"/></svg>
    <h1 class="hero-title" style="font-weight:400">Specialised learning<br>for children</h1>
    <span class="btn">Contact us</span>
  </section>

  <div class="abs why-kicker">WHY CHOOSE</div>
  <h2 class="abs why-title" style="font-weight:400">thebrightnook</h2>
  <div class="abs why-rule"></div>

  <article class="abs feature" style="left:18px">
    <svg class="feature-icon" viewBox="0 0 52 52"><circle cx="26" cy="26" r="25" fill="#fff" stroke="#7dc242" stroke-width="1.5"/><circle cx="26" cy="26" r="22" fill="#7dc242"/><circle cx="27" cy="16" r="3.5" fill="#fff"/><path d="M17 22 L27 22 L25 36 L20 38 L24 30 Z" fill="#fff"/></svg>
    <h3 class="feature-title" style="font-weight:400">ABOUT US</h3>
    <p class="feature-text">The way this program teaches and goes over the subject again if it was not understood is amazing! My son's reading comprehension was way below average. I now read the stories to him in the ninth grade Language Arts class, and there are many lessons on the one story. By the time he is done with the story,</p>
    <span class="btn-outline">Learn more</span>
  </article>

  <article class="abs feature" style="left:158px">
    <svg class="feature-icon" viewBox="0 0 52 52"><circle cx="26" cy="26" r="25" fill="#fff" stroke="#7dc242" stroke-width="1.5"/><circle cx="26" cy="26" r="22" fill="#7dc242"/><rect x="14" y="16" width="24" height="18" fill="none" stroke="#fff" stroke-width="1.5"/><line x1="18" y1="21" x2="34" y2="21" stroke="#fff"/><line x1="18" y1="25" x2="30" y2="25" stroke="#fff"/><circle cx="32" cy="31" r="3" fill="#fff"/></svg>
    <h3 class="feature-title" style="font-weight:400">CAREERS</h3>
    <p class="feature-text">The way this program teaches and goes over the subject again if it was not understood is amazing! My son's reading comprehension was way below average. I now read the stories to him in the ninth grade Language Arts class, and there are many lessons on the one story. By the time he is done with the story,</p>
    <span class="btn-outline">Learn more</span>
  </article>

  <article class="abs feature" style="left:296px">
    <svg class="feature-icon" viewBox="0 0 52 52"><circle cx="26" cy="26" r="25" fill="#fff" stroke="#7dc242" stroke-width="1.5"/><circle cx="26" cy="26" r="22" fill="#7dc242"/><rect x="14" y="15" width="24" height="17" fill="none" stroke="#fff" stroke-width="1.5"/><polyline points="17,28 22,23 26,26 33,19" fill="none" stroke="#fff" stroke-width="1.5"/><line x1="20" y1="32" x2="17" y2="39" stroke="#fff" stroke-width="1.5"/><line x1="32" y1="32" x2="35" y2="39" stroke="#fff" stroke-width="1.5"/></svg>
    <h3 class="feature-title" style="font-weight:400">TRAINING</h3>
    <p class="feature-text">The way this program teaches and goes over the subject again if it was not understood is amazing! My son's reading comprehension was way below average. I now read the stories to him in the ninth grade Language Arts class, and there are many lessons on the one story. By the time he is done with the story,</p>
    <span class="btn-outline">Learn more</span>
  </article>

  <section class="abs band">
    <div class="band-photo" role="img" aria-label="Photo of a teacher helping young children at a classroom table"></div>
    <div class="band-thumb" style="left:12px" role="img" aria-label="Classroom photo thumbnail"></div>
    <div class="band-thumb" style="left:85px" role="img" aria-label="Classroom photo thumbnail"></div>
    <div class="band-thumb" style="left:157px" role="img" aria-label="Classroom photo thumbnail"></div>
    <h2 class="band-title" style="font-weight:400">WHY CHOOSE THEBRIGHTNOOK</h2>
    <p class="band-text">The way this program teaches and goes over the subject again if it was not understood is amazing! My son's reading comprehension was way below average. I now read the stories to him in the ninth grade Language Arts class, and there are many lessons on the one story. By the time he is done with the story, he comprehends it one hundred percent. The way this program teaches and goes over the subject again if it was not understood is amazing! My son's reading comprehension was way below average. I now read the stories to him in the ninth grade Language Arts class, and there are many lessons.</p>
    <span class="btn">Learn more</span>
  </section>

  <section class="abs cta">
    <div class="cta-title">DO YOU STILL HAVE A QUESTTION REGARDING OUR SERVICES?</div>
    <div class="cta-text">The way this program teaches and goes over the subject again if it was not unde .....</div>
    <span class="cta-btn">CONTACT US</span>
  </section>

  <footer class="abs footer">
    <div class="footer-col" style="left:22px">
      <div class="footer-heading">Navigation</div>
      <ul class="footer-list"><li>HOME</li><li>TRAINING</li><li>STAFF</li><li>CONTACT US</li></ul>
    </div>
    <div class="footer-col" style="left:113px">
      <div class="footer-heading">Contact us</div>
      <div class="footer-contact">
        thebrightnook<br>your address,USA<br><br>
        <span class="label">Phone</span> : 555.014.2290<br>
        <span class="label">Fax</span> &nbsp;&nbsp;&nbsp;: 555.014.2290<br>
        <span class="label">Email</span> : hello@brightnookmail.com
      </div>
    </div>
    <div class="footer-col" style="left:224px">
      <div class="footer-heading">Contact us</div>
      <div class="footer-social"><span></span><span></span><span></span><span></span></div>
    </div>
    <div class="footer-brand"><span class="brand-dot"></span><span class="brand-name">thebrightnook</span></div>
  </footer>
</main>
</body>
</html>
```